Business Cards for business Personal Training, Group Fitness, Nutrition, Massage Business

In Bullet points on the back of the card please add the following:
12Week Body Transformation
Children's Fitness
Diet & Nutrition Plans
Exercise Plans
Fitness Events
Group Fitness
Massage
Mindset Lessons
Natural Health
Older Adult Fitness
Personal Training
Pre-Post Natal Pregnancy Fitness

Industry/Entity Type

Business

Contact Information for Business Card

Janet Holloway, Director & Health Coach
Mobile: 0481 567 392 | Email: Janet@bolthealthandfitness.com
Website: www.bolthealthandfitness.com
Sydney NSW 2000

Logo Text

BOLT Health and Fitness

Logo styles of interest
Character Logo
Wordmark Logo
Requirements
Must have
• Would like the business card to feature BOLT green as the main colour.
Would like to see a slogan on the business card also to appear after the business name. Slogan to read: helping you to get into BOLT condition
Nice to have
• If you choose an image, then please choose an image that represents Health and Fitness, Mind and Body well being
Should not have
• I do not have a logo pre-designed, so no logo required

```html
<!DOCTYPE html>
<html lang="en">
<head>
<meta charset="utf-8">
<title>Janet Holloway – BOLT Health and Fitness</title>
<link rel="stylesheet" href="https://fonts.googleapis.com/css2?family=Barlow:wght@400;500&display=swap">
<style>
  :root {
    --bolt-green: #a8ffb0;
    --ink-white: #ffffff;
  }
  html, body {
    margin: 0;
    padding: 0;
    width: 1200px;
    height: 693px;
    overflow: hidden;
    background: var(--bolt-green);
  }
  .business-card {
    display: block;
    width: 1200px;
    height: 693px;
    background: var(--bolt-green);
  }
  .card-text {
    font-family: "Barlow", "Helvetica Neue", Arial, sans-serif;
    fill: var(--ink-white);
  }
  .tagline { font-size: 52px; font-weight: 400; }
  .person-name { font-size: 122px; font-weight: 400; }
  .person-role { font-size: 37px; font-weight: 500; }
  .slogan { font-size: 28px; font-weight: 400; letter-spacing: 2px; }
  .service-item { font-size: 21px; font-weight: 400; letter-spacing: 1px; }
  .bullet { fill: var(--ink-white); }
  .contact-line { font-size: 26px; font-weight: 400; letter-spacing: 3px; }
  .contact-icon { fill: var(--ink-white); }
  .contact-icon-stroke { fill: none; stroke: var(--bolt-green); stroke-width: 2; }
  .globe-line { fill: none; stroke: var(--bolt-green); stroke-width: 1.6; }
</style>
</head>
<body>
<svg class="business-card" viewBox="0 0 1200 693" xmlns="http://www.w3.org/2000/svg">
  <rect width="1200" height="693" fill="var(--bolt-green)"/>

  <g class="card-header">
    <text class="card-text tagline" x="85" y="99" textLength="1041" lengthAdjust="spacing">For BOLT, Body and Spirit Wellbeing</text>
    <text class="card-text person-name" x="93" y="190" textLength="1008" lengthAdjust="spacing">Janet Holloway</text>
    <text class="card-text person-role" x="294" y="233" textLength="553" lengthAdjust="spacing">Director &amp; Health Coach</text>
    <text class="card-text slogan" x="600" y="286" text-anchor="middle">helping you to get into BOLT condition</text>
  </g>

  <g class="service-list">
    <g class="service-column">
      <circle class="bullet" cx="100" cy="331" r="4"/><text class="card-text service-item" x="114" y="338">12 Week Body Transformation</text>
      <circle class="bullet" cx="100" cy="365" r="4"/><text class="card-text service-item" x="114" y="372">Children's Fitness</text>
      <circle class="bullet" cx="100" cy="399" r="4"/><text class="card-text service-item" x="114" y="406">Diet &amp; Nutrition Plans</text>
      <circle class="bullet" cx="100" cy="433" r="4"/><text class="card-text service-item" x="114" y="440">Exercise Plans</text>
    </g>
    <g class="service-column">
      <circle class="bullet" cx="470" cy="331" r="4"/><text class="card-text service-item" x="484" y="338">Fitness Events</text>
      <circle class="bullet" cx="470" cy="365" r="4"/><text class="card-text service-item" x="484" y="372">Group Fitness</text>
      <circle class="bullet" cx="470" cy="399" r="4"/><text class="card-text service-item" x="484" y="406">Massage</text>
      <circle class="bullet" cx="470" cy="433" r="4"/><text class="card-text service-item" x="484" y="440">Mindset Lessons</text>
    </g>
    <g class="service-column">
      <circle class="bullet" cx="800" cy="331" r="4"/><text class="card-text service-item" x="814" y="338">Natural Health</text>
      <circle class="bullet" cx="800" cy="365" r="4"/><text class="card-text service-item" x="814" y="372">Older Adult Fitness</text>
      <circle class="bullet" cx="800" cy="399" r="4"/><text class="card-text service-item" x="814" y="406">Personal Training</text>
      <circle class="bullet" cx="800" cy="433" r="4"/><text class="card-text service-item" x="814" y="440">Pre-Post Natal Pregnancy Fitness</text>
    </g>
  </g>

  <g class="contact-list">
    <g class="phone-icon">
      <rect class="contact-icon" x="88" y="474" width="26" height="42" rx="4"/>
      <rect class="contact-icon" x="92" y="469" width="4" height="7"/>
      <rect x="92" y="480" width="18" height="11" rx="1" fill="var(--bolt-green)"/>
      <g fill="var(--bolt-green)">
        <circle cx="95" cy="497" r="1.5"/><circle cx="101" cy="497" r="1.5"/><circle cx="107" cy="497" r="1.5"/>
        <circle cx="95" cy="503" r="1.5"/><circle cx="101" cy="503" r="1.5"/><circle cx="107" cy="503" r="1.5"/>
        <circle cx="95" cy="509" r="1.5"/><circle cx="101" cy="509" r="1.5"/><circle cx="107" cy="509" r="1.5"/>
      </g>
    </g>
    <text class="card-text contact-line" x="128" y="519">0481 567 392</text>

    <g class="mail-icon">
      <rect class="contact-icon" x="81" y="540" width="37" height="24"/>
      <polyline class="contact-icon-stroke" points="82,541 99.5,556 117,541"/>
      <polyline class="contact-icon-stroke" points="82,563 94,551"/>
      <polyline class="contact-icon-stroke" points="117,563 105,551"/>
    </g>
    <text class="card-text contact-line" x="125" y="564">Janet@bolthealthandfitness.com</text>

    <g class="globe-icon">
      <circle class="contact-icon" cx="99" cy="600" r="18"/>
      <ellipse class="globe-line" cx="99" cy="600" rx="8" ry="18"/>
      <line class="globe-line" x1="99" y1="582" x2="99" y2="618"/>
      <line class="globe-line" x1="81" y1="600" x2="117" y2="600"/>
      <line class="globe-line" x1="84" y1="591" x2="114" y2="591"/>
      <line class="globe-line" x1="84" y1="609" x2="114" y2="609"/>
    </g>
    <text class="card-text contact-line" x="125" y="609">www.bolthealthandfitness.com</text>

    <g class="pin-icon">
      <path class="contact-icon" d="M99 632c-9 0-15 7-15 15 0 10 15 24 15 24s15-14 15-24c0-8-6-15-15-15z"/>
      <circle cx="99" cy="647" r="5" fill="var(--bolt-green)"/>
    </g>
    <text class="card-text contact-line" x="125" y="656">Sydney NSW 2000</text>
  </g>
</svg>
</body>
</html>
```